business card for a massage therapy practice named 'Meadow and Rowan Massage Studio'

I really need a trendy, yet easy on the eyes business card to complement my logo. Ideally with some gold or rose gold foil work.

My uploaded file of the logo I have in horizontal but I have a vertical version as well. Another color that is used in the website is a blush pink here and there. I'd like to see some trendy tropical leaves in the design.

```html
<!DOCTYPE html>
<html lang="en">
<head>
<meta charset="utf-8">
<title>Meadow and Rowan Massage Studio – Business Card</title>
<link rel="stylesheet" href="https://fonts.googleapis.com/css2?family=Source+Sans+3:wght@400;600&display=swap">
<style>
  :root {
    --leaf-deep: #1f4a44;
    --leaf-mid: #2f6b55;
    --card-paper: #ebe9e5;
    --ink-navy: #1e3b4c;
    --rule-navy: #1f3f4d;
    --rule-soft: #c9c7c3;
    --gold: #a8875a;
    --gold-dark: #6e5836;
    --blush: #e6957f;
  }
  * { margin: 0; padding: 0; box-sizing: border-box; }
  html, body { width: 1200px; height: 720px; overflow: hidden; background: #ffffff; }
  body { font-family: "Source Sans 3", sans-serif; color: var(--ink-navy); }

  .card { position: relative; width: 1200px; height: 720px; overflow: hidden; }

  .leaf-backdrop {
    position: absolute; inset: 0;
    background: radial-gradient(circle at 20% 30%, var(--leaf-mid), var(--leaf-deep) 70%);
  }

  .paper-panel {
    position: absolute; left: 69px; top: 69px; width: 1062px; height: 582px;
    background: var(--card-paper);
  }

  .pineapple-art {
    position: absolute; left: 286px; top: 107px; width: 107px; height: 296px;
    background: linear-gradient(180deg, #b39466 0%, var(--gold) 45%, #9c7d50 100%);
    border-radius: 46% 46% 44% 44% / 30% 30% 28% 28%;
  }

  .brand-name {
    position: absolute; left: 150px; top: 418px; width: 380px; text-align: center;
    font-size: 50px; font-weight: 400; color: var(--blush); line-height: 1;
  }
  .brand-tagline {
    position: absolute; left: 150px; top: 509px; width: 380px; text-align: center;
    font-size: 23px; letter-spacing: 0.5px; color: var(--gold-dark); line-height: 1;
  }
  .therapist-name {
    position: absolute; left: 150px; top: 551px; width: 380px; text-align: center;
    font-size: 20px; font-weight: 600; color: var(--gold); line-height: 1;
  }

  .info-rule {
    position: absolute; left: 601px; top: 119px; width: 4px; height: 465px;
    background: var(--rule-navy);
  }

  .hours-title {
    position: absolute; left: 621px; top: 126px;
    font-size: 22px; font-weight: 600; line-height: 1;
  }
  .hours-divider, .contact-divider {
    position: absolute; height: 1px; background: var(--rule-soft);
  }
  .hours-divider { left: 605px; top: 162px; width: 184px; }
  .contact-divider { left: 605px; top: 408px; width: 366px; }

  .hours-table {
    position: absolute; left: 621px; top: 185px;
    border-collapse: collapse; font-size: 22px; line-height: 31px;
  }
  .hours-table td { padding: 0; }
  .hours-table .day { width: 153px; }

  .contact-list { position: absolute; left: 621px; top: 428px; list-style: none; }
  .contact-item { display: flex; align-items: baseline; height: 36px; }
  .contact-label { width: 101px; font-size: 21px; }
  .contact-value { font-size: 19px; }

  .social-handle {
    position: absolute; right: 85px; top: 621px;
    display: flex; align-items: center; gap: 8px;
    font-size: 17px; color: var(--blush);
  }
  .social-dot { width: 14px; height: 14px; border-radius: 50%; background: var(--blush); }
</style>
</head>
<body>
  <main class="card">
    <div class="leaf-backdrop" role="img" aria-label="Dense pattern of tropical leaves and orange and coral flowers"></div>

    <section class="paper-panel"></section>

    <div class="pineapple-art" role="img" aria-label="Gold foil pineapple illustration"></div>
    <div class="brand-name">Meadow &amp; Rowan</div>
    <div class="brand-tagline">THE MASSAGE STUDIO</div>
    <div class="therapist-name">Dana Whitfield LMT</div>

    <div class="info-rule"></div>

    <h2 class="hours-title">Working Hours</h2>
    <div class="hours-divider"></div>
    <table class="hours-table">
      <tr><td class="day">Sunday</td><td>Closed</td></tr>
      <tr><td class="day">Monday</td><td>11:00 AM - 7:00 PM</td></tr>
      <tr><td class="day">Tuesday</td><td>11:00 AM - 7:00 PM</td></tr>
      <tr><td class="day">Wednesday</td><td>11:00 AM - 7:00 PM</td></tr>
      <tr><td class="day">Thursday</td><td>11:00 AM - 7:00 PM</td></tr>
      <tr><td class="day">Friday</td><td>11:00 AM - 7:00 PM</td></tr>
      <tr><td class="day">Saturday</td><td>11:00 AM - 7:00 PM</td></tr>
    </table>
    <div class="contact-divider"></div>

    <ul class="contact-list">
      <li class="contact-item"><span class="contact-label">Address:</span><span class="contact-value">2417 Linden Avenue, 210, Fairhaven, CA, 95020</span></li>
      <li class="contact-item"><span class="contact-label">Phone:</span><span class="contact-value">555-204-7718</span></li>
      <li class="contact-item"><span class="contact-label">Website:</span><span class="contact-value">www.meadowandrowan.com</span></li>
      <li class="contact-item"><span class="contact-label">Email:</span><span class="contact-value">hello@meadowandrowan.com</span></li>
    </ul>

    <div class="social-handle"><span class="social-dot"></span>@meadowandrowan</div>
  </main>
</body>
</html>
```